Business card design and logo needed

We have been operating as Ridgeline Paddock Fencing for 30 years but never had a logo and feel there is a need for one, but have no idea for a design.
We specialise in all types of rural fencing including post and wire, post and rail, electric, chainmesh and to a lesser extent, also do industrial security fencing.
Updates

Sorry, but website is ridgelinepaddock.net

No .au on the end!
My apologies

Regards, Barry

Target Market(s)

Rural/acreage property owners, particularly horse people.

Industry/Entity Type

Industrial

Contact Information for Business Card

Ridgeline Paddock Fencing Barry Lindqvist 0427 615302. Terry Lindqvist 0427 783160
Email: ridgelinepaddock@quolmail.com.au
Website: www.ridgelinepaddock.net

Requirements
Must have
• Would like to highlight website address - use the business card to advertise the website or to push them to check it out.

```html
<!DOCTYPE html>
<html lang="en">
<head>
<meta charset="utf-8">
<title>Ridgeline Paddock Fencing – Business Card</title>
<link rel="stylesheet" href="https://fonts.googleapis.com/css2?family=Open+Sans:wght@400;700&display=swap">
<style>
  :root {
    --backdrop: #2b3133;
    --card: #1b1e1f;
    --card-edge: #141617;
    --band: #1d241f;
    --band-line: #3a423c;
    --text-light: #d6d8d8;
    --text-mid: #a9adad;
    --logo-grey: #b9bcbc;
    --accent: #d07a1c;
    --divider: #8e9292;
  }
  * { box-sizing: border-box; margin: 0; padding: 0; }
  html, body {
    width: 1200px; height: 741px; overflow: hidden;
    background: var(--backdrop);
    font-family: "Open Sans", Verdana, sans-serif;
  }
  .sheet {
    position: relative; width: 1200px; height: 741px;
    display: flex; align-items: center; justify-content: center; gap: 40px;
  }
  .card {
    position: relative; width: 540px; height: 309px;
    background: var(--card);
    border: 1px solid var(--card-edge);
    box-shadow: 0 10px 30px rgba(0,0,0,.45);
    overflow: hidden;
  }
  .brand {
    display: flex; align-items: center; justify-content: center; gap: 12px;
  }
  .brand-mark {
    width: 16px; height: 16px; flex: none;
    background: var(--logo-grey);
  }
  .brand-name {
    font-weight: 400; color: var(--logo-grey);
    letter-spacing: .5px; white-space: nowrap;
  }
  /* back */
  .card--back { display: flex; flex-direction: column; align-items: center; justify-content: center; }
  .card--back .brand-name { font-size: 24px; }
  .card--back .web { margin-top: 34px; font-size: 15px; color: var(--accent); letter-spacing: 1px; }
  /* front */
  .card--front .band { position: absolute; inset: 0; }
  .card--front .brand {
    position: absolute; top: 62px; left: 0; right: 0;
  }
  .card--front .brand-name { font-size: 22px; }
  .contact { position: absolute; }
  .contact .name { font-weight: 700; font-size: 18px; line-height: 24px; color: var(--text-light); white-space: nowrap; }
  .contact .phone {
    display: flex; align-items: center; gap: 6px;
    font-size: 12px; line-height: 16px; color: var(--text-mid); margin-top: 1px;
  }
  .contact--left { right: 276px; top: 180px; text-align: right; }
  .contact--left .phone { justify-content: flex-end; }
  .contact--right { left: 298px; top: 146px; }
  .contact--right .phone { padding-left: 20px; }
  .divider {
    position: absolute; left: 282px; top: 172px; width: 1px; height: 54px;
    background: var(--divider);
  }
  .links { position: absolute; left: 196px; top: 238px; font-size: 12.5px; line-height: 18px; }
  .links li { list-style: none; display: flex; align-items: center; gap: 12px; margin-bottom: 3px; color: var(--text-light); white-space: nowrap; }
  .links .web { color: var(--accent); }
  .icon { width: 14px; height: 14px; flex: none; }
</style>
</head>
<body>
<main class="sheet">
  <section class="card card--back" aria-label="Card back">
    <div class="brand">
      <span class="brand-mark" aria-hidden="true"></span>
      <p class="brand-name">Ridgeline Paddock Fencing</p>
    </div>
    <p class="web">www.ridgelinepaddock.net</p>
  </section>

  <section class="card card--front" aria-label="Card front">
    <svg class="band" viewBox="0 0 540 309" preserveAspectRatio="none" aria-hidden="true">
      <path d="M0 0 H540 V60 Q300 175 0 160 Z" fill="var(--band)"/>
      <path d="M0 160 Q300 175 540 60" fill="none" stroke="var(--band-line)" stroke-width="2"/>
    </svg>
    <div class="brand">
      <span class="brand-mark" aria-hidden="true"></span>
      <p class="brand-name">Ridgeline Paddock Fencing</p>
    </div>

    <div class="contact contact--right">
      <p class="name">Terry Lindqvist</p>
      <p class="phone">
        <svg class="icon" viewBox="0 0 16 16" aria-hidden="true"><path d="M2 6c0-2 2-3 6-3s6 1 6 3l-2 1-1-2H5L4 7zM4 8h8l1 5H3z" fill="var(--text-mid)"/></svg>
        0427 783160
      </p>
    </div>
    <div class="divider"></div>
    <div class="contact contact--left">
      <p class="name">Barry Lindqvist</p>
      <p class="phone">
        <svg class="icon" viewBox="0 0 16 16" aria-hidden="true"><path d="M2 6c0-2 2-3 6-3s6 1 6 3l-2 1-1-2H5L4 7zM4 8h8l1 5H3z" fill="var(--text-mid)"/></svg>
        0427 615302
      </p>
    </div>

    <ul class="links">
      <li>
        <svg class="icon" viewBox="0 0 16 16" aria-hidden="true"><rect x="1.5" y="3.5" width="13" height="9" fill="none" stroke="var(--text-mid)"/><path d="M1.5 3.5 8 9l6.5-5.5" fill="none" stroke="var(--text-mid)"/></svg>
        ridgelinepaddock@quolmail.com.au
      </li>
      <li class="web">
        <svg class="icon" viewBox="0 0 16 16" aria-hidden="true"><circle cx="8" cy="8" r="6" fill="none" stroke="var(--text-mid)"/><ellipse cx="8" cy="8" rx="2.5" ry="6" fill="none" stroke="var(--text-mid)"/><path d="M2 8h12" stroke="var(--text-mid)"/></svg>
        www.ridgelinepaddock.net
      </li>
    </ul>
  </section>
</main>
</body>
</html>
```